Brook Outreach eCommerce (a-la-carte) Modern Edgy (Be Creative - Follow Brief)

//BROOK OUTREACH//
A-La-Carte style eCommerce site designed with pick and pay options. Full credit card payment gateway. Paypal offered, Google Pay, Apple Pay. (Open to suggestions: Wordpress, BigCommerce, Squarespace)

Designed to fit look and feel of logo. Warm, Inviting, Simple and Modern.

Pages (standard 5):
1. Main Page: Sample Cases/Photos, Hot Packages
2. About: Company statement, Staff bios, Our goals
3. Services: Place to list options, service offerings, prices of packages (ability to check out, pay, etc)
4. Portfolio: Place to showcase our work, testimonials, ratings
5. Contact: Contact form, Links to other platforms (Whatsapp, Telegram, Discord)

Links to Social Media, include ability to share throughout whole page.

***(See attached Logo - use for look and feel but feel free to be creative, only a suggestion)***

Target Market(s)

Business, Influencers, Brands

Industry/Entity Type

Branding & Marketing

Coding

Coded - Design and coding required

Number of Pages Required

5+ page

Colors
0054AA
0677BA
7BADD7
CADEEF
E8F1F8

Requirements
Must have
• Must be clean, easy to navigate, modern look and feel but warm and inviting
Nice to have
• Front Page - Main "HOT" offerings // About Page // Contact Page (Form - Links to Whatsapp, Telegram, Discord) // Services // Portfolio page -- Social Media Links
Should not have
• clutter.

```html
<!DOCTYPE html>
<html lang="en">
<head>
<meta charset="utf-8">
<title>Brook Outreach — About</title>
<link href="https://fonts.googleapis.com/css2?family=Playfair+Display:wght@500;600&family=Poppins:wght@300;400;500;600&display=swap" rel="stylesheet">
<style>
:root{
  --blue-deep:#0054AA;
  --blue:#0677BA;
  --blue-soft:#7BADD7;
  --blue-pale:#CADEEF;
  --blue-mist:#E8F1F8;
  --white:#ffffff;
  --ink:#1f3550;
  --muted:#5d7590;
}
*{box-sizing:border-box;margin:0;padding:0}
html,body{width:1200px;height:2692px;overflow:hidden}
body{background:var(--blue-mist);font-family:"Poppins",sans-serif;color:var(--ink);position:relative}
.abs{position:absolute}

/* header */
.site-header{left:0;top:0;width:1200px;height:220px}
.brand{left:140px;top:78px}
.brand-name{font-family:"Poppins",sans-serif;font-weight:600;font-size:64px;line-height:1;color:var(--blue-deep);letter-spacing:1px}
.main-nav{left:430px;top:50px;display:flex;gap:38px;font-size:15px;font-weight:500;color:var(--blue);letter-spacing:1px}
.nav-icons{left:946px;top:98px}
.login-btn{left:1000px;top:40px;width:92px;height:36px;border:2px solid var(--blue-deep);border-radius:4px;font-size:14px;font-weight:600;color:var(--blue-deep);display:flex;align-items:center;justify-content:center;letter-spacing:1px}

/* hero */
.hero{left:122px;top:253px;width:968px;height:330px;border-radius:6px;overflow:hidden;
  background:linear-gradient(100deg,#c9b8a6 0%,#d9cdbf 30%,#b7c7d6 60%,#a7bed3 100%)}
.hero-overlay{inset:0;background:rgba(232,241,248,.55)}
.hero-title{left:0;width:968px;top:66px;text-align:center;font-size:44px;font-weight:600;letter-spacing:6px;color:var(--blue)}
.hero-text{left:170px;top:148px;width:640px;font-size:19px;line-height:1.45;font-weight:500;color:var(--blue-deep)}
.hero-btn{left:438px;top:280px;width:92px;height:32px;background:var(--blue);color:var(--white);font-size:12px;display:flex;align-items:center;justify-content:center;border-radius:3px}

/* about */
.section-title{font-family:"Playfair Display",serif;font-weight:600;color:var(--blue);font-size:46px}
.swoosh{display:block}
.about-title{left:122px;top:668px}
.started-title{left:122px;top:790px;font-size:36px;letter-spacing:5px;color:var(--blue);font-weight:500}
.about-text{left:122px;top:868px;width:520px;font-size:14px;line-height:1.6;font-weight:500;color:var(--blue-deep)}
.stats-card{left:815px;top:645px;width:272px;height:505px;background:var(--white);box-shadow:0 6px 24px rgba(0,84,170,.15);text-align:center;padding-top:40px}
.stat{margin-bottom:44px}
.stat-label{font-size:14px;color:var(--blue);letter-spacing:1px}
.stat-value{font-size:30px;font-weight:600;color:var(--blue-deep);letter-spacing:2px;margin:8px 0}
.stat-note{font-size:13px;color:var(--blue);letter-spacing:1px}

/* goals */
.goals-title{left:515px;top:1040px}
.goals-art{left:128px;top:1155px;width:300px;height:265px;border:6px solid var(--white);box-shadow:0 6px 20px rgba(0,84,170,.18);background:linear-gradient(180deg,#4a3d86 0%,#5b4c9b 70%,#e9eef7 72%,#ffffff 100%)}
.goals-card{left:458px;top:1265px;width:625px;height:295px;background:var(--white);box-shadow:0 6px 24px rgba(0,84,170,.15);padding:62px 66px 0 66px;font-size:15px;line-height:1.6;font-weight:500;color:var(--blue-deep)}

/* team */
.team-title{left:118px;top:1510px}
.team-card{top:1670px;width:300px;height:510px;background:var(--white);box-shadow:0 6px 24px rgba(0,84,170,.15)}
.team-photo{width:300px;height:300px}
.team-name{margin:22px 20px 8px;font-size:17px;font-weight:600;color:var(--ink)}
.team-bio{margin:0 20px;font-size:14px;line-height:1.55;color:var(--muted)}
.team-more{left:127px;bottom:28px;width:46px;height:46px;border-radius:50%;background:var(--blue-pale);display:flex;align-items:center;justify-content:center}
.slider-arrow{top:1860px;width:52px;height:52px;border-radius:50%;background:var(--blue-pale);display:flex;align-items:center;justify-content:center}

/* footer */
.site-footer{left:0;top:2267px;width:1200px;height:425px;background:var(--blue-soft);color:var(--white)}
.footer-brand{left:90px;top:50px;font-size:36px;font-weight:600;line-height:1;color:var(--white)}
.footer-brand small{display:block;font-size:13px;letter-spacing:3px;font-weight:600;margin-top:4px}
.social-label{left:90px;top:160px;font-size:13px;letter-spacing:1px;font-weight:500}
.social-icons{left:90px;top:192px;display:flex;gap:18px}
.social-icons span{width:26px;height:26px;border-radius:50%;border:2px solid var(--white)}
.footer-col{top:50px;font-size:16px;line-height:2.15}
.footer-col h4{font-size:15px;font-weight:600;letter-spacing:1px;margin-bottom:4px}
.subscribe{left:735px;top:135px;display:flex}
.subscribe-input{width:238px;height:44px;background:var(--white);color:#9fb3c7;font-size:14px;display:flex;align-items:center;padding-left:20px}
.subscribe-btn{width:80px;height:44px;background:var(--blue-pale);color:var(--blue-deep);font-size:12px;font-weight:600;display:flex;align-items:center;justify-content:center}
.footer-rule{left:90px;top:330px;width:1020px;height:1px;background:rgba(255,255,255,.6)}
.legal{left:780px;top:338px;display:flex;gap:50px;font-size:13px;letter-spacing:1px}
</style>
</head>
<body>

<header class="abs site-header">
  <div class="abs brand"><span class="brand-name">brook</span></div>
  <nav class="abs main-nav"><span>HOME</span><span>ABOUT</span><span>SERVICES</span><span>PORTFOLIO</span><span>CONTACT</span></nav>
  <div class="abs nav-icons">
    <svg width="20" height="20" viewBox="0 0 20 20"><circle cx="8" cy="8" r="6" fill="none" stroke="#0677BA" stroke-width="2"/><line x1="12.5" y1="12.5" x2="18" y2="18" stroke="#0677BA" stroke-width="2"/></svg>
  </div>
  <div class="abs login-btn">LOGIN</div>
</header>

<section class="abs hero" role="img" aria-label="Group of smiling young people outdoors">
  <div class="abs hero-overlay"></div>
  <h1 class="abs hero-title">We Are Brook</h1>
  <p class="abs hero-text">Lorem Ipsum Dolor Sit Amet, Consectetur Adipiscing Elit. Quisque Volutpat In Erat In Ultrices. Ut Egestas Enim Quis Nisi Vestibulum, Ut Amet Semper Tortor Placerat. Cras Euismod Ut Leo At Convallis.</p>
  <div class="abs hero-btn">See More</div>
</section>

<section>
  <div class="abs about-title">
    <h2 class="section-title">About Us</h2>
    <svg class="swoosh" width="200" height="14"><path d="M2 9 Q100 1 198 7" stroke="#7BADD7" stroke-width="2" fill="none"/></svg>
  </div>
  <h3 class="abs started-title">HOW IT STARTED</h3>
  <p class="abs about-text">Ut At Ornare Est, Maecenas In Ex At Leo Mattis Tincidunt Vel Ac Orci. Quisque Scelerisque At Vitae Egestas Hendrerit. Suspendisse Congue Neque Vitae Dolor Vestibulum Placerat. Nullam Mollis Placerat Sem In Faucibus. Maecenas Hendrerit Mattis Metus Et Pellentesque. Morbi A Lacus Auctor, Pulvinar Justo In, Laoreet Enim. Cras Dignissim Tortor Lacus, Id Congue Est Dapibus Eu.</p>

  <aside class="abs stats-card">
    <div class="stat"><div class="stat-label">Launched In April Of</div><div class="stat-value">2022</div><div class="stat-note">Delivery From Day One</div></div>
    <div class="stat"><div class="stat-label">Our Product Powers</div><div class="stat-value">12,000+</div><div class="stat-note">Customer-Facing Teams</div></div>
    <div class="stat"><div class="stat-label">We Serve Customers In</div><div class="stat-value">50+</div><div class="stat-note">Countries</div></div>
  </aside>
</section>

<section>
  <div class="abs goals-title">
    <h2 class="section-title">Our Goals</h2>
    <svg class="swoosh" width="215" height="14"><path d="M2 9 Q108 1 213 7" stroke="#7BADD7" stroke-width="2" fill="none"/></svg>
  </div>
  <div class="abs goals-art" role="img" aria-label="Illustration of a red rocket launching above clouds"></div>
  <div class="abs goals-card">Ut At Ornare Est, Maecenas In Ex At Leo Mattis Tincidunt Vel Ac Orci. Quisque Scelerisque At Vitae Egestas Hendrerit. Suspendisse Congue Neque Vitae Dolor Vestibulum Placerat. Nullam Mollis Placerat Sem In Faucibus. Maecenas Hendrerit Mattis Metus Et Pellentesque. Morbi A Lacus Auctor, Pulvinar Justo In, Laoreet Enim. Cras Dignissim Tortor Lacus, Id Congue Est Dapibus Eu.</div>
</section>

<section>
  <div class="abs team-title">
    <h2 class="section-title">Our Teams</h2>
    <svg class="swoosh" width="215" height="14"><path d="M2 9 Q108 1 213 7" stroke="#7BADD7" stroke-width="2" fill="none"/></svg>
  </div>

  <div class="abs slider-arrow" style="left:30px"><svg width="16" height="16"><path d="M11 2 L5 8 L11 14" stroke="#fff" stroke-width="2.5" fill="none"/></svg></div>
  <div class="abs slider-arrow" style="left:1110px"><svg width="16" height="16"><path d="M5 2 L11 8 L5 14" stroke="#fff" stroke-width="2.5" fill="none"/></svg></div>

  <article class="abs team-card" style="left:118px">
    <div class="team-photo" role="img" aria-label="Portrait of a team member in a suit" style="background:linear-gradient(160deg,#8d8f92,#4c5561)"></div>
    <h4 class="team-name">Milo Carver</h4>
    <p class="team-bio">“ Lorem Ipsum Dolor Sit Amet, Consectetur Adipiscing Elit. Donec Cursus Pulvinar Ultrices.</p>
    <div class="abs team-more"><svg width="14" height="14"><path d="M2 7 H12 M8 3 L12 7 L8 11" stroke="#fff" stroke-width="2" fill="none"/></svg></div>
  </article>
  <article class="abs team-card" style="left:450px">
    <div class="team-photo" role="img" aria-label="Portrait of a team member in a denim jacket" style="background:linear-gradient(160deg,#c9b9a5,#6b7f9a)"></div>
    <h4 class="team-name">Milo Carver</h4>
    <p class="team-bio">“ Lorem Ipsum Dolor Sit Amet, Consectetur Adipiscing Elit. Donec Cursus Pulvinar Ultrices.</p>
    <div class="abs team-more"><svg width="14" height="14"><path d="M2 7 H12 M8 3 L12 7 L8 11" stroke="#fff" stroke-width="2" fill="none"/></svg></div>
  </article>
  <article class="abs team-card" style="left:785px">
    <div class="team-photo" role="img" aria-label="Portrait of a smiling team member" style="background:linear-gradient(160deg,#e6e2dc,#8a6a55)"></div>
    <h4 class="team-name">Milo Carver</h4>
    <p class="team-bio">“ Lorem Ipsum Dolor Sit Amet, Consectetur Adipiscing Elit. Donec Cursus Pulvinar Ultrices.</p>
    <div class="abs team-more"><svg width="14" height="14"><path d="M2 7 H12 M8 3 L12 7 L8 11" stroke="#fff" stroke-width="2" fill="none"/></svg></div>
  </article>
</section>

<footer class="abs site-footer">
  <div class="abs footer-brand">brook<small>OUTREACH</small></div>
  <div class="abs social-label">SOCIAL MEDIA</div>
  <div class="abs social-icons"><span></span><span></span><span></span></div>

  <div class="abs footer-col" style="left:405px"><h4>SHOP</h4><div>Products</div><div>Overview</div><div>Pricing</div><div>Releases</div></div>
  <div class="abs footer-col" style="left:560px"><h4>COMPANY</h4><div>About Us</div><div>Contact</div><div>News</div><div>Support</div></div>
  <div class="abs footer-col" style="left:735px"><h4>STAY UP TO DATE</h4></div>
  <div class="abs subscribe"><div class="subscribe-input">Enter Your Email</div><div class="subscribe-btn">SUBMIT</div></div>

  <div class="abs footer-rule"></div>
  <div class="abs legal"><span>TERMS</span><span>PRIVACY</span><span>COOKIES</span></div>
</footer>

</body>
</html>
```